Draft Beer System Services Sales Sheet

Wanting a sales sheet (leave behind) to match the glycol chiller maintenance sales sheet you created earlier this year (.pdf attached) for our company. I will upload a sketch with dialogue. I will also upload some relevant images. Can't wait to see this come together.

Target Market(s)

Bars, Brewery Tap Rooms, Restaurants, Sporting Venues

Industry/Entity Type

Draft Beer and Brewery Services

Font styles to use
Serif

Requirements
Must have
• Similar theme as previous sales sheet
Nice to have
• Images that seem relevant

```html
<!DOCTYPE html>
<html lang="en">
<head>
<meta charset="utf-8">
<title>Draft Beer System Service – Sales Sheet</title>
<link href="https://fonts.googleapis.com/css2?family=Oswald:wght@500;600;700&family=Montserrat:wght@400;500;600;700;800&display=swap" rel="stylesheet">
<style>
:root{
  --ink:#231f1e;
  --ink-2:#2e2a28;
  --gold:#f7a81b;
  --gold-light:#ffc533;
  --gold-deep:#e8900c;
  --grey:#8c8c8c;
  --grey-light:#e9e9e9;
  --white:#ffffff;
  --text-light:#f2f2f2;
  --heading-grey:#4f4f4f;
}
*{box-sizing:border-box;margin:0;padding:0}
html,body{width:1200px;height:2701px;overflow:hidden;background:var(--white)}
body{position:relative;font-family:'Montserrat',sans-serif}
.sheet{position:absolute;left:128px;width:944px;height:667px;background:var(--ink);overflow:hidden;box-shadow:0 2px 8px rgba(0,0,0,.15)}
.sheet--service{top:1073px}
.sheet--products{top:1862px}
.abs{position:absolute}
.photo{position:absolute}
.brand{position:absolute;display:flex;align-items:center;gap:9px;white-space:nowrap;font-family:'Montserrat',sans-serif;font-weight:800;font-size:22px;color:var(--heading-grey)}
.brand-dot{width:18px;height:18px;border-radius:50%;background:var(--gold);flex:none}
.seal{position:absolute;border-radius:50%;background:radial-gradient(circle,var(--gold-light),var(--gold-deep));border:5px solid var(--ink);box-shadow:0 0 0 3px var(--gold);display:flex;flex-direction:column;align-items:center;justify-content:center;color:var(--ink);font-weight:800;text-align:center}
.seal-small{font-size:10px;letter-spacing:1px}
.seal-big{font-family:'Oswald',sans-serif;font-size:38px;line-height:1}
.headline{position:absolute;font-family:'Oswald',sans-serif;font-weight:500;color:var(--ink);line-height:1;letter-spacing:-.5px;white-space:nowrap}
.pill{position:absolute;left:27px;width:302px;height:42px;border-radius:21px;background:linear-gradient(90deg,var(--gold-light),var(--gold));display:flex;align-items:center;gap:12px;padding-left:4px;white-space:nowrap;font-family:'Oswald',sans-serif;font-weight:500;font-size:19px;color:var(--ink)}
.pill-icon{width:34px;height:34px;border-radius:50%;background:var(--white);display:flex;align-items:center;justify-content:center;flex:none}
.cta{position:absolute;left:28px;top:550px;font-weight:800;font-size:21px;line-height:25px;color:var(--white)}
.cta span{color:var(--gold)}
.feature{position:absolute;width:270px}
.feature-title{display:flex;align-items:center;gap:8px;white-space:nowrap;font-weight:700;font-size:17px;color:var(--gold);margin-bottom:6px}
.feature-icon{width:36px;height:36px;border-radius:50%;background:var(--gold);display:flex;align-items:center;justify-content:center;flex:none}
.feature ul{list-style:none}
.feature li{position:relative;padding-left:16px;font-size:13.5px;line-height:16px;color:var(--text-light);margin-bottom:6px}
.feature li::before{content:"";position:absolute;left:0;top:4px;width:8px;height:8px;border-radius:50%;background:var(--gold)}
.feature li.plain::before{display:none}
.contact-phone{position:absolute;display:flex;align-items:center;gap:6px;white-space:nowrap;font-weight:800;color:var(--white)}
.contact-line{position:absolute;display:flex;align-items:center;gap:10px;white-space:nowrap;font-size:13px;color:var(--text-light)}
.web-pill{position:absolute;height:20px;border-radius:10px;background:var(--ink);border:2px solid var(--gold);display:flex;align-items:center;gap:8px;padding:0 10px;white-space:nowrap;font-size:13px;letter-spacing:4px;color:var(--text-light)}
.web-pill b{font-weight:800}
.products-title{position:absolute;left:300px;top:44px;font-family:'Oswald',sans-serif;font-weight:700;font-size:80px;letter-spacing:-1px;color:var(--heading-grey);line-height:1;white-space:nowrap}
.tile{position:absolute;width:162px;height:142px;border:4px solid #b8963a;border-radius:10px}
.caption{position:absolute;width:180px;text-align:center;font-size:13.5px;line-height:16px;color:var(--text-light)}
.footer-contact{position:absolute;left:28px;top:628px;font-weight:800;font-size:30px;color:var(--ink);white-space:nowrap}
</style>
</head>
<body>

<section class="sheet sheet--service" aria-label="Draft beer system service sheet">
  <svg class="abs" width="944" height="667" style="left:0;top:0">
    <rect x="0" y="0" width="944" height="667" fill="#231f1e"/>
    <path d="M330 0 H944 V200 Q700 175 330 245 Z" fill="#ffffff"/>
    <path d="M330 0 H700 L690 25 L715 60 L690 95 L710 130 L680 175 Q500 185 330 215 Z" fill="#f7a81b"/>
    <path d="M330 215 Q600 165 944 200 V215 Q620 180 330 240 Z" fill="#8c8c8c"/>
    <path d="M570 667 V560 Q610 470 740 455 Q870 450 944 520 V667 Z" fill="#f7a81b"/>
  </svg>
  <div class="photo" role="img" aria-label="Row of wooden-handled draft beer taps on a bar wall" style="left:0;top:0;width:335px;height:330px;background:linear-gradient(160deg,#6b5a4a,#b9b3ab 55%,#3a3330);border-bottom-right-radius:40px"></div>
  <div class="photo" role="img" aria-label="Chrome beer tower with taps over a drip tray" style="left:580px;top:466px;width:364px;height:201px;border-top-left-radius:190px 200px;background:linear-gradient(180deg,#d9d7d3,#6d6a66 70%,#3a3735)"></div>

  <h1 class="headline" style="left:358px;top:40px;font-size:52px">DRAFT BEER<br>SYSTEM SERVICE</h1>

  <div class="brand" style="left:725px;top:105px"><span class="brand-dot"></span>The Tap Crew</div>

  <div class="seal" style="left:182px;top:170px;width:142px;height:142px">
    <span class="seal-small">SATISFACTION</span>
    <span class="seal-big">100%</span>
    <span class="seal-small">GUARANTEED</span>
  </div>

  <div class="pill" style="top:374px"><span class="pill-icon"><svg width="20" height="20" viewBox="0 0 20 20"><circle cx="10" cy="10" r="6" fill="none" stroke="#231f1e" stroke-width="3"/><circle cx="10" cy="10" r="2" fill="#231f1e"/></svg></span>SYSTEM EXPERTS</div>
  <div class="pill" style="top:431px"><span class="pill-icon"><svg width="20" height="20" viewBox="0 0 20 20"><circle cx="10" cy="5" r="3" fill="#231f1e"/><circle cx="4" cy="14" r="2.5" fill="#231f1e"/><circle cx="16" cy="14" r="2.5" fill="#231f1e"/><circle cx="10" cy="14" r="2.5" fill="#231f1e"/></svg></span>INDUSTRY LEADING KNOWLEDGE</div>
  <div class="pill" style="top:488px"><span class="pill-icon"><svg width="20" height="20" viewBox="0 0 20 20"><circle cx="10" cy="8" r="5" fill="none" stroke="#231f1e" stroke-width="2.5"/><path d="M3 17 H17" stroke="#231f1e" stroke-width="3"/></svg></span>EXCELLENT SERVICE</div>

  <p class="cta">CONTACT THE TAP CREW<br><span>TODAY TO SCHEDULE YOUR<br>MAINTENANCE PROGRAM</span></p>

  <div class="feature" style="left:372px;top:222px">
    <div class="feature-title"><span class="feature-icon"><svg width="18" height="18" viewBox="0 0 18 18"><rect x="6" y="2" width="6" height="14" fill="#231f1e"/></svg></span>SYSTEM DESIGN</div>
    <ul><li>Baverage Dispensing Design</li><li>Bar &amp; walk-in cooler layout</li><li>Designated contact to work with your team</li></ul>
  </div>
  <div class="feature" style="left:644px;top:222px">
    <div class="feature-title"><span class="feature-icon"><svg width="18" height="18" viewBox="0 0 18 18"><path d="M3 3 L15 15 M15 3 L3 15" stroke="#231f1e" stroke-width="2.5"/></svg></span>SYSTEM INSTALLATION</div>
    <ul><li>Perfectly balanced dispense system</li><li>Installed by Certified Draft system Installers</li><li>Superior Dispense Equipment</li><li class="plain">304 Grade stainless steel</li><li>Glycol Chiller warranty 1yr Parts 3yr Compressor</li></ul>
  </div>
  <div class="feature" style="left:372px;top:365px;width:270px">
    <div class="feature-title"><span class="feature-icon"><svg width="18" height="18" viewBox="0 0 18 18"><rect x="3" y="3" width="12" height="12" rx="2" fill="none" stroke="#231f1e" stroke-width="2.5"/></svg></span>MAINTENANCE SERVICES</div>
    <ul><li>Annual Glycol Chiller maintenance</li><li>Draft Beer Systems Trouble shooting &amp; Evaluation</li><li>Draft line bi-weekly maintenance</li><li>Gas Belnder &amp; Gas Regulator Service &amp; Repair</li></ul>
  </div>

  <div class="contact-phone" style="left:352px;top:545px;font-size:25px"><svg width="22" height="22" viewBox="0 0 22 22"><circle cx="11" cy="11" r="10" fill="none" stroke="#f7a81b" stroke-width="2.5"/><path d="M7 6 Q7 15 16 15 L16 12 L13 11 L12 12 Q9 11 9 9 L10 8 L9 6 Z" fill="#f7a81b"/></svg>555-014-2290</div>
  <div class="contact-line" style="left:362px;top:579px"><svg width="12" height="14" viewBox="0 0 12 14"><path d="M6 0 A5 5 0 0 1 11 5 Q11 9 6 14 Q1 9 1 5 A5 5 0 0 1 6 0Z" fill="#f7a81b"/><circle cx="6" cy="5" r="2" fill="#231f1e"/></svg>P.O. Box 12, Millbrook, OH 40001</div>
  <div class="web-pill" style="left:344px;top:610px;width:236px"><svg width="12" height="12" viewBox="0 0 12 12"><circle cx="6" cy="6" r="5" fill="#f7a81b"/></svg>www.<b>tapcrew</b>.net</div>
</section>

<section class="sheet sheet--products" aria-label="Products sheet">
  <svg class="abs" width="944" height="667" style="left:0;top:0">
    <defs><linearGradient id="topfade" x1="0" y1="0" x2="0" y2="1"><stop offset="0" stop-color="#e4e4e4"/><stop offset="1" stop-color="#f7f7f7"/></linearGradient></defs>
    <rect width="944" height="667" fill="#231f1e"/>
    <path d="M0 0 H944 V225 Q600 185 200 225 L0 225 Z" fill="url(#topfade)"/>
    <path d="M0 0 H180 L290 60 L300 200 L0 240 Z" fill="#f7a81b"/>
    <path d="M200 225 Q600 180 944 225 V238 Q600 200 200 240 Z" fill="#8c8c8c"/>
    <path d="M0 622 H230 L245 667 H0 Z" fill="#ffffff"/>
    <path d="M230 622 H944 V667 H245 Z" fill="#f7a81b"/>
  </svg>
  <div class="photo" role="img" aria-label="Black tap handles with chrome faucets" style="left:0;top:20px;width:225px;height:380px;background:linear-gradient(170deg,#2a2727,#555 50%,#a8a39d)"></div>

  <div class="seal" style="left:158px;top:28px;width:100px;height:100px">
    <span class="seal-small" style="font-size:8px">SATISFACTION</span>
    <span class="seal-big" style="font-size:28px">100%</span>
    <span class="seal-small" style="font-size:8px">GUARANTEED</span>
  </div>

  <h1 class="products-title">PRODUCTS</h1>
  <div class="brand" style="left:725px;top:106px"><span class="brand-dot"></span>The Tap Crew</div>

  <div class="tile" role="img" aria-label="Bar taps dispensing wine" style="left:200px;top:222px;background:linear-gradient(#4a4644,#cfcac4)"></div>
  <div class="tile" role="img" aria-label="Cocktail tap tower on a bar" style="left:383px;top:222px;background:linear-gradient(#8a6e54,#3c3430)"></div>
  <div class="tile" role="img" aria-label="Nitro cold brew tap wall with purple light" style="left:565px;top:222px;background:linear-gradient(#3b3440,#9a8fb0)"></div>
  <div class="tile" role="img" aria-label="Custom copper draft tower" style="left:748px;top:222px;background:linear-gradient(#5a2f24,#b0683c)"></div>
  <div class="caption" style="left:191px;top:371px">Wine on top</div>
  <div class="caption" style="left:374px;top:371px">Cocktails on top</div>
  <div class="caption" style="left:556px;top:371px">Nitro Cold Brew<br>on top</div>
  <div class="caption" style="left:739px;top:371px">Customized Draft<br>tower &amp; Equipment</div>

  <div class="tile" role="img" aria-label="Gas lines and cylinders in a service room" style="left:20px;top:420px;background:linear-gradient(#cfcfd4,#6a6f80)"></div>
  <div class="tile" role="img" aria-label="Chrome faucet in a lit bar" style="left:200px;top:420px;background:linear-gradient(#2e3b57,#b58a3a)"></div>
  <div class="tile" role="img" aria-label="Copper water dispense towers" style="left:383px;top:420px;background:linear-gradient(#d9d6d2,#8a6a55)"></div>
  <div class="tile" role="img" aria-label="Brick walk-in cooler tap wall" style="left:565px;top:420px;background:linear-gradient(#6d4a3a,#3a3533)"></div>
  <div class="tile" role="img" aria-label="Long bar with gas blending system" style="left:748px;top:420px;background:linear-gradient(#3b4a55,#bfb8ae)"></div>
  <div class="caption" style="left:11px;top:569px">Annual &amp; Bi-annual<br>Service agreements</div>
  <div class="caption" style="left:191px;top:569px">CO<sub style="font-size:9px">2</sub> Alarm<br>systems</div>
  <div class="caption" style="left:374px;top:569px">Water Dispense<br>Towers</div>
  <div class="caption" style="left:556px;top:569px">Walk-in Cooler<br>design</div>
  <div class="caption" style="left:739px;top:569px">Customized gas<br>blending</div>

  <div class="footer-contact">Contact us</div>
  <div class="contact-phone" style="left:240px;top:633px;font-size:20px;color:var(--ink)"><svg width="20" height="20" viewBox="0 0 22 22"><circle cx="11" cy="11" r="10" fill="none" stroke="#fff" stroke-width="2.5"/><path d="M7 6 Q7 15 16 15 L16 12 L13 11 L12 12 Q9 11 9 9 L10 8 L9 6 Z" fill="#fff"/></svg>555-014-2290 &nbsp;|</div>
  <div class="contact-line" style="left:435px;top:637px;color:var(--ink)"><svg width="12" height="14" viewBox="0 0 12 14"><path d="M6 0 A5 5 0 0 1 11 5 Q11 9 6 14 Q1 9 1 5 A5 5 0 0 1 6 0Z" fill="#fff"/><circle cx="6" cy="5" r="2" fill="#f7a81b"/></svg>P.O. Box 12, Millbrook, OH 40001</div>
  <div class="web-pill" style="left:668px;top:634px;width:276px;height:22px;border:none;border-radius:11px 0 0 11px"><svg width="12" height="12" viewBox="0 0 12 12"><circle cx="6" cy="6" r="5" fill="#f7a81b"/></svg>www.<b>tapcrew</b>.net</div>
</section>

</body>
</html>
```